Stationery for London Estate Agents (Real Estate)

We are a modern and professional Estate Agency (Realtors) working with high quality properties in London.
We wish to redesign our stationary using our branding displayed on the front of our offices and require a digital version of this logo to be produced (photograph attached). Slight 'tweaking' of this branding is acceptable.
Updates
1st July 2010 Thank you all those designers who have uploaded submissions. Business Card - Details Side: Business Card - Logo Side: Outline of London Skyline Examples of the london skyline are available at http://www.pictovantix.com/searchkwy_london-skyline-silhouette Please be advised that we are looking for an outline, not a 'filled in' silhouette. Letterhead Please feel free to ask us any questions. Bertrand
I have been able to further refine our design requirements based on your submissions.
We like Pale Forks' business card submission that has not been eliminated and have the following design clarifications;
a) Please use an email icon (e.g an envelope).
b) Please make the email as equally prominent as the telephone and fax
c) We very much like VelloTrine's 'mini window icon' - please display the website URL under such a mini window icon at the bottom right of the card.
We are very happy with the colouring, fonts and proportions used by Pale Forks.
We invite designers to try adding an outline of the London Skyline to the left of the large window icon on the business card and in a suitablie position on the Letterhead (e.g at the top left of the letterhead).
We have the following design clarifiications to our Letterhead requirements;
A) We would like the main logo to be on the top right side of the letterhead.
B) We do NOT want the large window icon to be on the left of the logo or the bottom of the letterhead. We are happy having the large window icon to the right or underneath the KB brand.
C) Please use icons for tel, fax and email (e.g. envelope icon for e-mail address)
D) We like two coloured red borders, one at the top and bottom of the letterhead but are happy for variations in shape and size.
E) We currently prefer our address and contact details at the bottom of the letterhead.
F) We like VelloTrine's 'mini window icon' and would prefer this to be used to display the website URL at the bottom right of the letterhead.
G) Please be advised that the letterhead does NOT need additional space for the Company Name as per Pale Forks' submission - the KB brand is sufficient.
Target Market(s)
Owners of high quality property in London.
Industry/Entity Type
Real Estate
Requirements
Must have
- Business Cards: We would like a 'vertical' style business card with our branding on one side and our staff's details on the other;
- Our website is www.korbend.com and we are flexible where that should be on the card and letterhead.
- Stationery details are available in a file attached to this project.
Nice to have
- It would be great to have a horizontal version of the digital logo for placement on property portals (150x60)
Should not have
- Logo should not deviate significantly from the branding on our offices (shop front) - photograph attached.

```html
<!DOCTYPE html>
<html lang="en">
<head>
<meta charset="utf-8">
<title>Korbend Homes – Business Card Options</title>
<link rel="stylesheet" href="https://fonts.googleapis.com/css2?family=Arimo:wght@400;700&display=swap">
<style>
  :root {
    --brand-red: #870000;
    --brand-yellow: #fde800;
    --ink: #000000;
    --paper: #ffffff;
    --text-grey: #9a9a9a;
    --text-light: #b0b0b0;
  }
  * { margin: 0; padding: 0; box-sizing: border-box; }
  html, body { width: 866px; height: 1200px; overflow: hidden; background: var(--paper); }
  body { position: relative; font-family: "Arimo", Arial, sans-serif; }

  .side-label {
    position: absolute; width: 300px; text-align: center;
    font-weight: 700; font-size: 40px; line-height: 40px; color: var(--ink);
  }
  .card {
    position: absolute; width: 291px; height: 405px;
    box-shadow: 3px 4px 5px rgba(0,0,0,.45); overflow: hidden;
  }
  .card--front { background: var(--brand-red); }
  .card--back { background: var(--paper); border: 1px solid #666; }

  .brand-name {
    position: absolute; left: 0; width: 100%; text-align: center;
    font-size: 39px; line-height: 40px; font-weight: 400; letter-spacing: 0.2px;
  }
  .card--front .brand-name { color: var(--paper); }
  .card--back .brand-name { color: var(--brand-red); }

  .service-band {
    position: absolute; left: -2px; top: 133px; width: 293px; height: 131px;
    background: var(--brand-yellow); box-shadow: 2px 3px 4px rgba(0,0,0,.35);
  }
  .service-list {
    position: absolute; left: 42px; list-style: none;
    color: var(--paper); font-weight: 700; font-size: 22px; line-height: 29.3px;
  }
  .service-list--shadowed { text-shadow: 1px 2px 3px rgba(0,0,0,.55); }
  .service-list li::before { content: "• "; }

  .brand-square { position: absolute; background: var(--brand-yellow); }

  .contact { position: absolute; color: var(--text-grey); }
  .contact__name { font-weight: 700; font-size: 27px; line-height: 30px; }
  .contact__mobile { font-size: 15px; line-height: 18px; }
  .contact__address { color: var(--text-light); font-size: 12px; line-height: 16px; }
  .contact__lines { font-size: 12px; line-height: 16px; }
  .contact b { font-weight: 700; }
  .contact--wide .contact__name { font-size: 24px; line-height: 26px; }
  .contact--wide .contact__address,
  .contact--wide .contact__lines { font-size: 13.5px; line-height: 17px; }
</style>
</head>
<body>

  <!-- Option one -->
  <div class="side-label" style="left:126px; top:98px;">FRONT</div>
  <div class="side-label" style="left:461px; top:98px;">BACK</div>

  <section class="card card--front" style="left:126px; top:148px;">
    <div class="brand-name" style="top:25px;">KORBEND<br>HOMES</div>
    <div class="service-band"></div>
    <ul class="service-list service-list--shadowed" style="top:138px;">
      <li>Sales</li><li>Lettings</li><li>Management</li><li>Investments</li>
    </ul>
    <div class="brand-square" style="left:176px; top:312px; width:80px; height:80px;"></div>
  </section>

  <section class="card card--back" style="left:471px; top:148px;">
    <div class="brand-name" style="top:25px;">KORBEND<br>HOMES</div>
    <div class="contact" style="left:29px; top:145px;">
      <div class="contact__name">Bertrand Hale</div>
      <div class="contact__mobile"><b>Mobile:</b> 07700 900 415</div>
      <div class="contact__address" style="margin-top:60px;">42 Elmstead Road<br>Larchmere<br>London, SW14 6RJ</div>
      <div class="contact__lines" style="margin-top:5px;"><b>Tel:</b> (020 7946 0400)<br><b>Fax:</b> (020 7946 0522)</div>
      <div class="contact__lines" style="margin-top:6px;"><b>Email:</b><br>(bertrand@korbend.com)<br><b>Web:</b> www.korbend.com</div>
    </div>
    <div class="brand-square" style="left:198px; top:300px; width:80px; height:80px;"></div>
  </section>

  <!-- Option two -->
  <div class="side-label" style="left:126px; top:652px;">FRONT</div>
  <div class="side-label" style="left:461px; top:652px;">BACK</div>

  <section class="card card--front" style="left:126px; top:703px;">
    <div class="brand-name" style="top:22px;">KORBEND<br>HOMES</div>
    <ul class="service-list" style="left:42px; top:136px; font-size:23px;">
      <li>Sales</li><li>Lettings</li><li>Management</li><li>Investments</li>
    </ul>
    <div class="brand-square" style="left:172px; top:306px; width:82px; height:82px;"></div>
  </section>

  <section class="card card--back" style="left:471px; top:703px;">
    <div class="brand-name" style="top:22px;">KORBEND<br>HOMES</div>
    <div class="contact contact--wide" style="left:49px; top:134px;">
      <div class="contact__name">Bertrand Hale</div>
      <div class="contact__lines"><b>Mobile:</b> 07700 900 415</div>
      <div class="contact__address" style="margin-top:8px;">42 Elmstead Road<br>Larchmere<br>London, SW14 6RJ</div>
      <div class="contact__lines" style="margin-top:8px;"><b>Tel:</b> 020 7946 0400<br><b>Fax:</b> 020 7946 0522</div>
      <div class="contact__lines" style="margin-top:8px;"><b>Email:</b> bertrand@korbend.com<br><b>Web:</b> www.korbend.com</div>
    </div>
  </section>

</body>
</html>
```